International Lifestyle Households Brand Needs a Sticker for a New Product

We want a set of die cut sticker in 4 color versions for a collection of infuser mug which are in ceramic and glass mug. The size must be within 10 x 10cm. Since the mug colors are not warm and cozy to home (black, white, glass) but no outstanding in retail space, our objective is to stand out the products by the colorful sticker with simple graphic of its unique selling point.

There is also a COFFEE Version, KELP POUROVER CUP and we need the sticker with similar content. We would like to assign the sticker design to the same design who pick the job of TAVO STEEPER CUP.

We are the brand originated from Denmark. The final design should communicate our brand value: safety, health and design. The fonts for the main tagline must be DIN medium. The format and design should be minimal, clean and organic in style. We would like to see design that use Magenta, Blue, Green and Orange, but other options are welcome.

Target Market(s)

Global

Industry/Entity Type

Product

Font styles to use
Other font styles liked:
• Din Medium

Colors
e34297
33a6d7
f37122
86cfc6

Requirements
Must have
• Must have points have been included in the Design Briefing-Stikcer of Tavo Steeper Cup.pdf
Nice to have
• Illustration that fully demonstrate the USP

```html
<!DOCTYPE html>
<html lang="en">
<head>
<meta charset="utf-8">
<title>Tavo Steeper Cup – Sticker Set</title>
<link href="https://fonts.googleapis.com/css2?family=Barlow:wght@500;600&display=swap" rel="stylesheet">
<style>
  :root {
    --magenta: #e34297;
    --blue: #33a6d7;
    --green: #86cfc6;
    --orange: #f37122;
    --white: #ffffff;
    --ink: #2b2b2b;
    --page: #ffffff;
  }
  * { margin: 0; padding: 0; box-sizing: border-box; }
  html, body {
    width: 800px; height: 1200px; overflow: hidden;
    background: var(--page);
    font-family: "Barlow", sans-serif;
  }
  .sticker-set {
    width: 800px; height: 1200px;
    display: grid;
    grid-template-columns: 1fr 1fr;
    grid-template-rows: 1fr 1fr;
    place-items: center;
  }
  .sticker { width: 320px; height: 300px; }
  .sticker svg { width: 100%; height: 100%; display: block; }
  .sticker--magenta { --tone: var(--magenta); }
  .sticker--blue { --tone: var(--blue); }
  .sticker--green { --tone: var(--green); }
  .sticker--orange { --tone: var(--orange); }
  .sticker__shape { fill: var(--tone); stroke: var(--tone); stroke-width: 44; stroke-linejoin: round; }
  .sticker__panel { fill: var(--white); }
  .sticker__usp-art { fill: var(--tone); opacity: .35; }
  .sticker__name { font-family: "Barlow", sans-serif; font-weight: 500; font-size: 15px; fill: var(--tone); }
  .sticker__detail { font-family: "Barlow", sans-serif; font-weight: 500; font-size: 10px; fill: var(--white); }
  .sticker__badge { fill: var(--white); }
  .sticker__tick { fill: none; stroke: var(--tone); stroke-width: 2; stroke-linecap: round; stroke-linejoin: round; }
</style>
</head>
<body>
<main class="sticker-set">

  <figure class="sticker sticker--magenta">
    <svg viewBox="0 0 320 300">
      <polygon class="sticker__shape" points="160,28 292,262 28,262"/>
      <rect class="sticker__panel" x="124" y="82" width="72" height="72" rx="8"/>
      <rect class="sticker__usp-art" x="132" y="90" width="56" height="56" rx="5" role="img" aria-label="Simple illustration of the mug with its tea infuser"/>
      <rect class="sticker__panel" x="82" y="166" width="156" height="24" rx="3"/>
      <text class="sticker__name" x="160" y="183" text-anchor="middle">Tavo Steeper Cup</text>
      <text class="sticker__detail" x="160" y="210" text-anchor="middle">350 ml  Lead free</text>
      <circle class="sticker__badge" cx="146" cy="232" r="10"/>
      <path class="sticker__tick" d="M141 232 l4 4 l7 -8"/>
      <circle class="sticker__badge" cx="174" cy="232" r="10"/>
      <path class="sticker__tick" d="M169 232 l4 4 l7 -8"/>
    </svg>
  </figure>

  <figure class="sticker sticker--blue">
    <svg viewBox="0 0 320 300">
      <polygon class="sticker__shape" points="160,28 292,262 28,262"/>
      <rect class="sticker__panel" x="124" y="82" width="72" height="72" rx="8"/>
      <rect class="sticker__usp-art" x="132" y="90" width="56" height="56" rx="5" role="img" aria-label="Simple illustration of the mug with its tea infuser"/>
      <rect class="sticker__panel" x="82" y="166" width="156" height="24" rx="3"/>
      <text class="sticker__name" x="160" y="183" text-anchor="middle">Tavo Steeper Cup</text>
      <text class="sticker__detail" x="160" y="210" text-anchor="middle">350 ml  Lead free</text>
      <circle class="sticker__badge" cx="146" cy="232" r="10"/>
      <path class="sticker__tick" d="M141 232 l4 4 l7 -8"/>
      <circle class="sticker__badge" cx="174" cy="232" r="10"/>
      <path class="sticker__tick" d="M169 232 l4 4 l7 -8"/>
    </svg>
  </figure>

  <figure class="sticker sticker--green">
    <svg viewBox="0 0 320 300">
      <polygon class="sticker__shape" points="160,28 292,262 28,262"/>
      <rect class="sticker__panel" x="124" y="82" width="72" height="72" rx="8"/>
      <rect class="sticker__usp-art" x="132" y="90" width="56" height="56" rx="5" role="img" aria-label="Simple illustration of the mug with its tea infuser"/>
      <rect class="sticker__panel" x="82" y="166" width="156" height="24" rx="3"/>
      <text class="sticker__name" x="160" y="183" text-anchor="middle">Tavo Steeper Cup</text>
      <text class="sticker__detail" x="160" y="210" text-anchor="middle">350 ml  Lead free</text>
      <circle class="sticker__badge" cx="146" cy="232" r="10"/>
      <path class="sticker__tick" d="M141 232 l4 4 l7 -8"/>
      <circle class="sticker__badge" cx="174" cy="232" r="10"/>
      <path class="sticker__tick" d="M169 232 l4 4 l7 -8"/>
    </svg>
  </figure>

  <figure class="sticker sticker--orange">
    <svg viewBox="0 0 320 300">
      <polygon class="sticker__shape" points="160,28 292,262 28,262"/>
      <rect class="sticker__panel" x="124" y="82" width="72" height="72" rx="8"/>
      <rect class="sticker__usp-art" x="132" y="90" width="56" height="56" rx="5" role="img" aria-label="Simple illustration of the mug with its tea infuser"/>
      <rect class="sticker__panel" x="82" y="166" width="156" height="24" rx="3"/>
      <text class="sticker__name" x="160" y="183" text-anchor="middle">Tavo Steeper Cup</text>
      <text class="sticker__detail" x="160" y="210" text-anchor="middle">350 ml  Lead free</text>
      <circle class="sticker__badge" cx="146" cy="232" r="10"/>
      <path class="sticker__tick" d="M141 232 l4 4 l7 -8"/>
      <circle class="sticker__badge" cx="174" cy="232" r="10"/>
      <path class="sticker__tick" d="M169 232 l4 4 l7 -8"/>
    </svg>
  </figure>

</main>
</body>
</html>
```